Newsletter-Design für Garten-Samen Shop
Zielgruppe
Online Shop für Obst-, Gemüse-, Kräuter- und Pflanzensamen
Aufgabenstellung
www.beetfreunde-portal.example ist die Seite mit den Produkten. Als Tipp sollte das Jiaogulan genannt werden da dieses Produkt sich am meisten verkauft.

```html
<!DOCTYPE html>
<html lang="de">
<head>
<meta charset="utf-8">
<title>Beetfreunde Newsletter</title>
<link href="https://fonts.googleapis.com/css2?family=Lato:wght@400;700&family=Roboto:wght@400;700&family=Ubuntu:ital,wght@0,400;0,500;0,700;1,300&display=swap" rel="stylesheet">
<style>
:root{
  --page:#ececec;
  --card:#ffffff;
  --green:#7cb41c;
  --orange:#f39323;
  --ink:#2d2d2d;
  --muted:#666666;
  --purple:#955a96;
  --button:#8c6489;
  --tab:#efefef;
  --footer:#8e6f8c;
  --footer-dark:#7e627c;
  --contact-ink:#8f6a8c;
}
*{box-sizing:border-box;margin:0;padding:0}
html,body{width:1200px;height:4016px;overflow:hidden;background:var(--page)}
.stage{position:absolute;left:0;top:0;width:770px;height:2577px;transform:scale(1.5584);transform-origin:0 0;font-family:'Roboto',sans-serif;color:var(--ink)}
.newsletter{position:absolute;left:185px;top:101px;width:400px;height:2365px;background:var(--card);box-shadow:0 0 6px rgba(0,0,0,.12);overflow:hidden}
.abs{position:absolute}
.brand{left:27px;top:10px}
.brand-name{font-family:'Lato',sans-serif;font-weight:700;font-size:21px;color:var(--green);letter-spacing:.3px;line-height:24px}
.brand-tag{font-family:'Lato',sans-serif;font-size:10.5px;margin-left:3px;line-height:13px}
.contact-top{right:12px;top:11px;text-align:right;font-family:'Lato',sans-serif}
.contact-top .label{font-size:12px;line-height:14px}
.contact-top .phone{font-size:12.5px;font-weight:700;color:var(--orange);line-height:15px;letter-spacing:-.3px}
.hero{left:0;top:55px;width:400px;height:200px;background:
 radial-gradient(circle at 15% 20%,#e8792b 0,transparent 30%),
 radial-gradient(circle at 45% 20%,#b8232b 0,transparent 22%),
 radial-gradient(circle at 85% 15%,#f3a024 0,transparent 22%),
 radial-gradient(circle at 10% 80%,#5f8e3a 0,transparent 30%),
 radial-gradient(circle at 55% 80%,#e8c21c 0,transparent 22%),
 radial-gradient(circle at 85% 75%,#8bb83a 0,transparent 28%),
 linear-gradient(120deg,#b8542a,#a13a2e 50%,#6e8d34)}
.hero-title{left:0;top:78px;width:400px;text-align:center;color:#fff;text-shadow:0 1px 3px rgba(0,0,0,.7)}
.hero-title .l1{font-weight:700;font-size:16px;line-height:20px}
.hero-title .l2{font-size:15.5px;line-height:19px}
.intro{left:12px;top:273px;width:376px}
.intro h2{font-size:10.5px;font-weight:700;line-height:13px}
.intro p{font-size:7.4px;line-height:11.8px;color:#333}
.intro p+p{margin-top:12px}
.btn{display:inline-block;background:var(--button);color:#fff;font-family:'Ubuntu',sans-serif;font-size:10px;border-radius:2px;text-align:center}
.intro .btn{margin-top:12px;width:64px;height:25px;line-height:25px;background:var(--purple)}
.tabs{left:12px;top:422px;display:flex;gap:12px}
.tab{width:85px;height:30px;background:var(--tab);color:var(--purple);font-family:'Ubuntu',sans-serif;font-size:11px;text-transform:uppercase;text-align:center;line-height:31px}
.section-title{left:0;top:481px;width:400px;text-align:center;font-family:'Lato',sans-serif;font-weight:700;font-size:16.5px;letter-spacing:.3px}
.products{left:12px;top:523px;width:376px;display:grid;grid-template-columns:179px 179px;column-gap:18px;grid-auto-rows:290px}
.product{position:relative}
.product .photo{height:114px}
.price{height:24px;background:var(--purple);color:#fff;text-align:center;font-family:'Ubuntu',sans-serif;line-height:25px}
.price i{font-weight:300;font-size:12px}
.price b{font-weight:700;font-size:15px}
.price s{font-size:10px;font-weight:300;margin-left:2px}
.product h3{margin-top:11px;font-family:'Ubuntu',sans-serif;font-weight:500;font-size:10px;line-height:12.5px;height:28px}
.product p{margin-top:6px;font-size:7.2px;line-height:11.8px;color:var(--muted);height:52px}
.product .btn{position:absolute;left:0;top:238px;width:75px;height:23px;line-height:23px;font-size:9.5px}
.contact{left:0;top:1980px;width:400px;height:186px;text-align:center;background:
 radial-gradient(circle at 10% 30%,#f6dfe2 0,transparent 35%),
 radial-gradient(circle at 90% 40%,#f4e4d6 0,transparent 35%),
 radial-gradient(circle at 50% 90%,#eadff0 0,transparent 40%),
 linear-gradient(90deg,#f7eef2,#f1e8ef 50%,#f6ece8)}
.contact .call{margin-top:17px;font-family:'Ubuntu',sans-serif;font-size:10.5px;color:#9a8298;line-height:13px}
.contact .bignum{font-family:'Ubuntu',sans-serif;font-weight:700;font-size:22px;color:var(--contact-ink);line-height:26px}
.contact .company{font-size:8.5px;font-weight:700;line-height:11px;margin-top:2px}
.contact .addr{font-size:8.5px;line-height:11px}
.contact .mail{font-family:'Ubuntu',sans-serif;font-style:italic;font-weight:300;font-size:8.5px;line-height:15px;margin-top:6px;color:#555}
.socials{display:flex;justify-content:center;gap:11px;margin-top:10px}
.socials span{width:32px;height:32px;border-radius:50%;border:1px solid #c9b2c6}
.footer{left:0;top:2166px;width:400px;height:165px;background:var(--footer);color:#fff;font-size:8.3px}
.col{position:absolute;top:20px;line-height:16.6px}
.col h4{font-family:'Ubuntu',sans-serif;font-weight:400;font-size:10px;line-height:16px;margin-top:-1px}
.copyright{left:0;top:2331px;width:400px;height:34px;background:var(--footer-dark);color:#fff;font-size:7.5px;text-align:center;line-height:34px}
</style>
</head>
<body>
<div class="stage">
<div class="newsletter">
  <div class="abs brand">
    <div class="brand-name">BEETFREUNDE</div>
    <div class="brand-tag">Obst, Gemüse + Pflanzen</div>
  </div>
  <div class="abs contact-top">
    <div class="label">Telefon</div>
    <div class="phone">0123 45678901</div>
  </div>

  <div class="abs hero" role="img" aria-label="Foto: frisches Obst und Gemüse – Karotten, Granatapfel, Paprika, Äpfel, Kohl"></div>
  <div class="abs hero-title">
    <div class="l1">Obst-, Gemüse-, Pflanzen- und Kräuter-Samen</div>
    <div class="l2">aus dem eigenen Garten</div>
  </div>

  <div class="abs intro">
    <h2>Obst und Gemüse aus dem eigenen Garten ist immer toll,</h2>
    <p>denn da weiß man was auf den Teller kommt. Zudem schmeckt es frisch aus dem Garten ohnehin besser als aus dem Supermarkt. Wer Kinder hat, kann Obst und Gemüse zusammen mit den Kindern pflanzen. Die Kleinen sehen dann die Erfolge und lernen Pflanzen auch als Lebewesen kennen, die wachsen.</p>
    <p>Viele schreckt der Aufwand ab, dabei muss ein Obst- und Gemüsebeet gar nicht viel Arbeit machen. Unser Tipp: Jiaogulan – unser meistverkauftes Produkt, pflegeleicht und ideal für Einsteiger.</p>
    <span class="btn">Weiterlesen</span>
  </div>

  <div class="abs tabs">
    <div class="tab">Obst</div><div class="tab">Gemüse</div><div class="tab">Pflanzen</div><div class="tab">Kräuter</div>
  </div>

  <div class="abs section-title">TOP BELIEBTESTE PRODUKTE</div>

  <div class="abs products">
    <div class="product">
      <div class="photo" role="img" aria-label="Foto: Venusfliegenfalle" style="background:linear-gradient(160deg,#3e5a1e,#b5c83a 45%,#e0d640 60%,#4a6a1c)"></div>
      <div class="price"><i>ab</i> <b>9.99€</b></div>
      <h3>Venusfliegenfalle – Insektenfressende Pflanze – ca. 50 Stück</h3>
      <p>50 Samen der Venusfliegenfalle oder auch Insektenfressende Pflanze zum selbst aussähen. Die Venusfliegenfalle ist die einzige ihrer Art unter den fleischfressenden Pflanzen.</p>
      <span class="btn">zum Angebot</span>
    </div>
    <div class="product">
      <div class="photo" role="img" aria-label="Foto: große rote Tomate in Händen" style="background:radial-gradient(circle at 50% 55%,#d8321c 0,#c22a18 28%,#6a6a6a 48%,#3a3a3a)"></div>
      <div class="price"><i>ab</i> <b>3,99€</b></div>
      <h3>Riesen Tomaten – roter saftiger Riese<br>(ca. 50 Samen)</h3>
      <p>50 Samen von Riesen Tomaten zum selbst aussähen. Diese Tomate ist eine sehr aromatische Sorte, die riesengroße rote saftige Tomaten bildet. Die Pflanze ist sehr früh mit langem.</p>
      <span class="btn">zum Angebot</span>
    </div>
    <div class="product">
      <div class="photo" role="img" aria-label="Foto: blühender Bärlauch" style="background:linear-gradient(135deg,#2f5a22,#6f9a4a 40%,#4c7a32 70%,#24461a)"></div>
      <div class="price"><i>ab</i> <b>3,49€</b></div>
      <h3>Bärlauch / Waldknoblauch – ca. 50<br>Samen</h3>
      <p>50 Samen vom Bärlauch – auch Waldknoblauch genannt – zum selbst aussähen. Bärlauch besitzt ähnliche Heil- und Gewürzwirkung wie Knoblauch. Die jungen,</p>
      <span class="btn">zum Angebot</span>
    </div>
    <div class="product">
      <div class="photo" role="img" aria-label="Foto: Kräutertöpfe auf einem Tisch" style="background:linear-gradient(120deg,#b89468,#9bbf3a 40%,#5e8a2a 65%,#c9a77a)"></div>
      <div class="price"><i>ab</i> <b>6,99€</b></div>
      <h3>Kräuterpaket – 5 Kräuter ca. 350<br>Samen – Ideal für die Fensterbank</h3>
      <p>350 Samen von 5 verschiedenen Kräutern als Kräuterpaket zum selbst aussähen. Wer frisch kocht, möchte auch gerne frische Kräuter an sein essen haben und keine getrockneten.</p>
      <span class="btn">zum Angebot</span>
    </div>
    <div class="product">
      <div class="photo" role="img" aria-label="Foto: Sonnenblume" style="background:radial-gradient(circle at 50% 45%,#f2d21a 0,#e8b818 30%,#9aa43a 60%,#c9c46a)"></div>
      <div class="price"><i>ab</i> <b>2.99€</b></div>
      <h3>Sonnenblumen Samen (Helianthus<br>annuus) – ca. 50 Stück, gelb, gross</h3>
      <p>50 Samen der Sonnenblume zum selbst aussähen. Die Sonnenblumen sind seit jeher ein Hingucker in jedem Garten. Jeder kennt sie und jeder liebt sie. Sonnenblumen sind toll und bringen Lebensfreude.</p>
      <span class="btn">zum Angebot</span>
    </div>
    <div class="product">
      <div class="photo" role="img" aria-label="Foto: blaue Kornblume" style="background:radial-gradient(circle at 45% 50%,#6a5ad0 0,#4a3c90 25%,#3a3a28 60%,#5a5a3a)"></div>
      <div class="price"><i>ab</i> <b>3.99€</b></div>
      <h3>Kornblume (Centaurea cyanus)<br>a. 50 Samen</h3>
      <p>50 Samen der Kornblume zum selbst aussähen. Die Kornblume mit ihren blauen bis violetten Blütenkörben dürfte den meisten im deutschen Sprachraum bekannt sein.</p>
      <span class="btn">zum Angebot</span>
    </div>
    <div class="product">
      <div class="photo" role="img" aria-label="Foto: großer Kürbis vor Holzstapel" style="background:linear-gradient(180deg,#6a4a32,#8a6a4a 45%,#e8862a 70%,#b8602a)"></div>
      <div class="price"><i>ab</i> <b>7.49€</b></div>
      <h3>Riesen Kürbis – (ca. 50 Samen)</h3>
      <p>50 Samen von Riesen Kürbis zum selbst aussähen. Der orange Riesenkürbis ist ein richtig leckerer Speisekürbis, der den herbstlichen Speiseplan vitaminreich ergänzt. Natürlich ist er auch als Herbstdeko eine echte Zierde.</p>
      <span class="btn">zum Angebot</span>
    </div>
    <div class="product">
      <div class="photo" role="img" aria-label="Foto: Mandarinenbaum mit Früchten vor blauem Himmel" style="background:radial-gradient(circle at 40% 40%,#f0902a 0,transparent 25%),radial-gradient(circle at 70% 65%,#ee8a24 0,transparent 22%),linear-gradient(180deg,#4a78c8,#3a6a2a 50%,#5a8ad0)"></div>
      <div class="price"><i>ab</i> <b>6,99€</b> <s>7,99 €</s></div>
      <h3>Mandarinenbaum (Citrus reticulata)<br>ca. 50 Samen</h3>
      <p>50 Samen von Mandarinenbaum zum selbst aussähen. Der Mandarinenbaum ist mit seinem stark buschigen Wachstum sowie den elliptischen, dunkelgrün-glänzenden.</p>
      <span class="btn">zum Angebot</span>
    </div>
    <div class="product">
      <div class="photo" role="img" aria-label="Foto: rote Blüten des Flammenbaums" style="background:linear-gradient(135deg,#d8241c,#4a6a2a 45%,#e0301e 70%,#3a5a22)"></div>
      <div class="price"><i>ab</i> <b>4.49€</b></div>
      <h3>Flammenbaum – (Delonix regia)<br>ca. 10 Samen</h3>
      <p>10 Samen vom Flammenbaum zum selbst aussähen. Der Flammenbaum wächst als Baum, der Wuchshöhen von 12 bis 17 Metern – aber auch als Bonsai geeignet.</p>
      <span class="btn">zum Angebot</span>
    </div>
    <div class="product">
      <div class="photo" role="img" aria-label="Foto: rosa Blüten des Trompetenbaums" style="background:linear-gradient(135deg,#f2c6d8,#e8a6c4 45%,#f6dbe6 70%,#c88aa8)"></div>
      <div class="price"><i>ab</i> <b>5,99€</b> <s>6,99 €</s></div>
      <h3>Trompetenbaum – (Tabebuia<br>impetiginosa) – ca. 10 Samen</h3>
      <p>10 Samen vom Trompetenbaum zum selbst aussähen. Der Trompetenbaum ist ein bis zu 30m hoher Baum mit rundlicher stark verzweigter Baumkrone.</p>
      <span class="btn">zum Angebot</span>
    </div>
  </div>

  <div class="abs contact">
    <div class="call">RUF UNS HEUTE AN</div>
    <div class="bignum">0123 45678901</div>
    <div class="company">Samenhof GmbH</div>
    <div class="addr">diese vertreten durch den Geschäftsführer Jonas Wellbrock Lindenweg 12</div>
    <div class="addr">12345 Musterfeld Deutschland</div>
    <div class="mail">info@samenhof.example<br>www.beetfreunde-portal.example</div>
    <div class="socials"><span></span><span></span><span></span><span></span><span></span></div>
  </div>

  <div class="abs footer">
    <div class="col" style="left:12px">Startseite<br>Obst<br>Gemüse<br>Kräuter<br>Pflanzen<br>Shop<br>Warenkorb<br>Impressum</div>
    <div class="col" style="left:110px"><h4>KATEGORIEN</h4>Gemüse<br>Kräuter<br>Obst<br>Pflanzen</div>
    <div class="col" style="left:204px"><h4>NEUESTE BEITRÄGE</h4>Flammenbaum (Delonix regia)<br>Kornblume (Centaurea cyanus)<br>Mandarinenbaum (Citrus reticulata)<br>Trompetenbaum (Catalpa bignonioides)<br>Schnittlauch (Allium schoenoparsum)</div>
  </div>
  <div class="abs copyright">Copyright ©&nbsp; Beetfreunde 2017</div>
</div>
</div>
</body>
</html>
```